Business card for a young aspring actress

My daughter is 18 and just starting out on her profession as an actress. She is a member of the Harbour Young Players and has already had some extras work and a featured role in an upcoming Feature film.

She wants/needs a card that she can have to hand to give to those she comes into contact with in the theatre, TV and film industries.

We are thinking that it may be double sided with an impact side including a picture of her and her name etc with the reverse holding contact and other details.

She wants to go by the name Maya Louise Brennick.

She has done a little modelling but sees herself as an actress.

She can be seen in this video
http://www.oakvalepark-academy.org/videos/be0881e4276ee2512c50a07f907c1d03?width=640&height=480

Target Market(s)

Anyone she comes into contact with in theatre TV and film industries.

Industry/Entity Type

Business

Requirements
Nice to have
• She has email and a website www.mayabrennick.com She is quite a connected girl

```html
<!DOCTYPE html>
<html lang="en">
<head>
<meta charset="utf-8">
<title>Maya Louise Brennick – Business Card</title>
<link href="https://fonts.googleapis.com/css2?family=Michroma&family=Open+Sans+Condensed:wght@300&family=Open+Sans:wght@400&display=swap" rel="stylesheet">
<style>
  :root {
    --page-bg: #e9e9e9;
    --card-maroon: #5c2b33;
    --banner-rose: #c96262;
    --banner-rose-light: #d46d6b;
    --name-maroon: #6a2f38;
    --paper-white: #ffffff;
    --photo-light: #e6e6e6;
    --photo-mid: #a9a9a9;
    --photo-dark: #4a4a4a;
    --icon-rose: #c45d5d;
  }
  * { box-sizing: border-box; margin: 0; padding: 0; }
  html, body { width: 1200px; height: 1000px; overflow: hidden; }
  body {
    background: radial-gradient(ellipse at center, #f6f6f6 0%, var(--page-bg) 70%, #d9d9d9 100%);
    position: relative;
    font-family: "Open Sans", Arial, sans-serif;
  }
  .card {
    position: absolute;
    top: 100px;
    width: 370px;
    height: 800px;
    overflow: hidden;
    box-shadow: 0 6px 18px rgba(0,0,0,0.18);
  }
  .card--front { left: 190px; background: var(--paper-white); }
  .card--back  { left: 640px; background: var(--card-maroon); }

  /* Front */
  .front-portrait {
    position: absolute; inset: 0;
    background:
      radial-gradient(ellipse 55% 40% at 55% 40%, #f4f4f4 0%, transparent 70%),
      linear-gradient(105deg, var(--photo-dark) 0%, var(--photo-mid) 30%, var(--photo-light) 55%, var(--photo-mid) 80%, #6b6b6b 100%);
  }
  .front-portrait::after {
    content: ""; position: absolute; left: 0; right: 0; bottom: 0; height: 45%;
    background: linear-gradient(to bottom, transparent, rgba(245,245,245,0.9));
  }
  .front-name {
    position: absolute; right: 24px; bottom: 70px;
    text-align: right;
    font-family: "Michroma", "Arial Narrow", sans-serif;
    font-size: 27px; line-height: 1.2; letter-spacing: 1px;
    color: var(--name-maroon);
    text-transform: uppercase;
  }

  /* Back */
  .name-banner { position: absolute; top: 0; left: 0; width: 370px; height: 270px; }
  .back-name {
    position: absolute; top: 70px; right: 44px;
    text-align: right;
    font-family: "Michroma", "Arial Narrow", sans-serif;
    font-size: 24px; line-height: 1.25; letter-spacing: 1px;
    color: var(--paper-white);
    text-transform: uppercase;
  }
  .portrait-frame {
    position: absolute; left: 85px; top: 300px;
    width: 250px; height: 250px; border-radius: 50%;
    background: var(--paper-white);
    padding: 12px;
  }
  .portrait-circle {
    width: 100%; height: 100%; border-radius: 50%;
    background: linear-gradient(110deg, var(--photo-mid) 0%, var(--photo-light) 45%, #cfcfcf 70%, var(--photo-dark) 100%);
  }
  .contact-list {
    position: absolute; left: 28px; top: 600px;
    list-style: none;
  }
  .contact-item {
    display: flex; align-items: center; gap: 10px;
    margin-bottom: 10px;
    font-family: "Open Sans Condensed", "Arial Narrow", sans-serif;
    font-weight: 300; font-size: 17px; letter-spacing: 0.3px;
    color: var(--paper-white);
    text-transform: uppercase;
  }
  .contact-icon {
    width: 22px; height: 22px; border-radius: 4px;
    background: var(--icon-rose);
    display: flex; align-items: center; justify-content: center;
    flex: none;
  }
</style>
</head>
<body>

<section class="card card--front">
  <div class="front-portrait" role="img" aria-label="Black and white portrait photograph of the actress filling the card"></div>
  <p class="front-name">Maya<br>Louise<br>Brennick</p>
</section>

<section class="card card--back">
  <svg class="name-banner" viewBox="0 0 370 270" aria-hidden="true">
    <defs>
      <linearGradient id="bannerFill" x1="0" y1="0" x2="1" y2="1">
        <stop offset="0" stop-color="var(--banner-rose-light)"/>
        <stop offset="1" stop-color="var(--banner-rose)"/>
      </linearGradient>
    </defs>
    <polygon points="70,20 356,20 356,240 200,240 70,200" fill="#f2f2f2"/>
    <polygon points="62,12 342,12 342,228 196,228 62,188" fill="url(#bannerFill)"/>
    <polygon points="62,188 196,228 196,240 62,200" fill="#f2f2f2"/>
  </svg>
  <p class="back-name">Maya<br>Louise<br>Brennick</p>

  <div class="portrait-frame">
    <div class="portrait-circle" role="img" aria-label="Circular black and white portrait photograph of the actress"></div>
  </div>

  <ul class="contact-list">
    <li class="contact-item">
      <span class="contact-icon">
        <svg width="14" height="14" viewBox="0 0 14 14"><path d="M1 7 L7 1.5 L13 7 H11 V12.5 H8.5 V9 H5.5 V12.5 H3 V7 Z" fill="#fff"/></svg>
      </span>
      14 Quay Row, Harbourton HB4 2QT
    </li>
    <li class="contact-item">
      <span class="contact-icon">
        <svg width="14" height="14" viewBox="0 0 14 14"><path d="M3 1.5 L5.5 1.5 L6.5 4.5 L5 5.8 C5.8 7.6 6.6 8.5 8.2 9.2 L9.5 7.6 L12.5 8.6 L12.5 11 C12.5 12 11.6 12.6 10.6 12.4 C5.8 11.4 2.6 8.2 1.6 3.4 C1.4 2.4 2 1.5 3 1.5 Z" fill="#fff"/></svg>
      </span>
      0700.555.214
    </li>
    <li class="contact-item">
      <span class="contact-icon">
        <svg width="14" height="14" viewBox="0 0 14 14"><text x="7" y="11" text-anchor="middle" font-family="Arial, sans-serif" font-size="12" fill="#fff">@</text></svg>
      </span>
      info@mayabrennick.tv
    </li>
    <li class="contact-item">
      <span class="contact-icon">
        <svg width="14" height="14" viewBox="0 0 14 14" fill="none" stroke="#fff" stroke-width="1.2"><circle cx="7" cy="7" r="5.5"/><ellipse cx="7" cy="7" rx="2.4" ry="5.5"/><line x1="1.5" y1="7" x2="12.5" y2="7"/></svg>
      </span>
      www.mayabrennick.tv
    </li>
  </ul>
</section>

</body>
</html>
```